TL Estates
Desmond Parkes
TL Estates - Real Estate
Creative Brief
Corporate
Owner/ Realtor
Suite # 17 Ashbury Business Centre, 28 Calder Rd. Kingston 5
dp@desmondparkes-example.com
www.desmondparkes-example.com
Business card , Letter head and envelopes to compliment LOGO i DO NOT WANT MY PICTURE TO APPEAR IN A BOX...I WOULD WANT IT TO BE FLOATING ON THE BUSINESS CARD I would like for the designers to colour my shirt RED

```html
<!DOCTYPE html>
<html lang="en">
<head>
<meta charset="utf-8">
<title>TL Estates Stationery</title>
<link href="https://fonts.googleapis.com/css2?family=Open+Sans:wght@400;600;700&display=swap" rel="stylesheet">
<style>
:root{
  --bg:#3a3a3c;
  --paper:#ffffff;
  --red:#b3121b;
  --red-dark:#6d0a10;
  --ink:#333333;
  --muted:#8a8a8a;
  --black:#141414;
  --caption:#bdbdbd;
}
*{margin:0;padding:0;box-sizing:border-box}
html,body{width:1200px;height:341px;overflow:hidden;background:var(--bg);font-family:"Open Sans",Arial,sans-serif;color:var(--ink)}
.canvas{position:relative;width:1200px;height:341px}
.item{position:absolute;background:var(--paper);overflow:hidden;box-shadow:0 2px 6px rgba(0,0,0,.45)}
.wave{position:absolute;left:0;bottom:0;width:100%;display:block}
.mark{display:flex;flex-direction:column;align-items:center;gap:2px}
.mark-square{background:var(--red)}
.mark-name{color:var(--red);font-weight:700;letter-spacing:.4px;white-space:nowrap;text-transform:uppercase;line-height:1}
.caption{position:absolute;color:var(--caption);font-size:6px;line-height:8px;text-align:center;white-space:nowrap}
.watermark{position:absolute;display:flex;flex-direction:column;align-items:center;gap:3px;opacity:.09}
.contact{position:absolute;font-size:3.4px;line-height:4.6px;color:var(--muted);white-space:nowrap}

/* brand block */
.brand{position:absolute;left:24px;top:22px;width:70px}
.brand .mark-square{width:46px;height:46px}
.brand .mark-name{font-size:8px;margin-top:3px}
.brand .tagline{font-size:3.6px;color:var(--muted);letter-spacing:.4px;white-space:nowrap}
.brand-caption{left:24px;top:88px;width:70px}

/* business card */
.card-front{left:34px;top:196px;width:158px;height:44px}
.card-front .mark{position:absolute;left:7px;top:5px}
.card-front .mark-square{width:10px;height:10px}
.card-front .mark-name{font-size:3.6px}
.card-front .holder{position:absolute;left:7px;top:22px;font-size:3.4px;line-height:4.4px;white-space:nowrap}
.card-front .holder b{color:var(--red);font-size:4.2px}
.portrait{position:absolute;left:96px;top:4px;width:24px;height:32px;border-radius:12px 12px 0 0;background:linear-gradient(180deg,#caa08a 0%,#caa08a 40%,#c0161f 42%,#8c0d14 100%)}
.card-caption{left:34px;top:242px;width:158px}

.card-back{left:34px;top:254px;width:158px;height:39px}
.card-back .mark{position:absolute;left:50%;top:7px;transform:translateX(-50%)}
.card-back .mark-square{width:12px;height:12px}
.card-back .mark-name{font-size:4.2px}
.card-back .tagline{font-size:2.8px;color:var(--muted);letter-spacing:.3px;white-space:nowrap}
.card-back-caption{left:34px;top:295px;width:158px}

/* letterheads */
.letterhead{top:19px;width:175px;height:293px}
.letterhead-one{left:233px}
.letterhead-two{left:425px}
.letterhead .mark{position:absolute;left:12px;top:10px}
.letterhead .mark-square{width:11px;height:11px}
.letterhead .mark-name{font-size:3.8px}
.letterhead .contact{left:112px;top:10px}
.letterhead .watermark{left:50%;top:112px;transform:translateX(-50%)}
.letterhead .watermark .mark-square{width:40px;height:40px}
.letterhead .watermark .mark-name{font-size:8px}

/* envelopes front */
.envelope{left:655px;width:238px}
.envelope-one{top:65px;height:98px}
.envelope-two{top:204px;height:96px}
.envelope .mark{position:absolute}
.envelope-one .mark{left:10px;top:8px}
.envelope-two .mark{left:10px;top:20px}
.envelope .mark-square{width:10px;height:10px}
.envelope .mark-name{font-size:3.6px}
.envelope .watermark{left:50%;top:28px;transform:translateX(-50%)}
.envelope-two .watermark{left:auto;right:30px;top:26px;transform:none}
.envelope .watermark .mark-square{width:26px;height:26px}
.envelope .watermark .mark-name{font-size:5px}

/* envelopes back */
.envelope-back{left:910px;width:261px}
.envelope-back-flap{top:53px;height:110px}
.envelope-back-plain{top:204px;height:96px;background:#f3f3f3}
.flap{position:absolute;left:0;top:0;width:100%;display:block}
.envelope-back .mark{position:absolute;left:50%;top:52px;transform:translateX(-50%)}
.envelope-back .mark-square{width:9px;height:9px}
.envelope-back .mark-name{font-size:3.6px}
</style>
</head>
<body>
<main class="canvas">

  <section class="brand">
    <div class="mark">
      <div class="mark-square"></div>
      <div class="mark-name">TL Estates</div>
      <div class="tagline">SALES · RENTALS · VALUATIONS</div>
    </div>
  </section>
  <p class="caption brand-caption">Preferred Concept</p>

  <article class="item card-front">
    <div class="mark"><div class="mark-square"></div><div class="mark-name">TL Estates</div></div>
    <div class="holder"><b>Desmond Parkes</b><br>Owner / Realtor<br>876-555-0142</div>
    <div class="portrait" role="img" aria-label="Floating cut-out photo of the realtor wearing a red shirt"></div>
    <svg class="wave" viewBox="0 0 100 14" preserveAspectRatio="none" height="9">
      <path d="M0 6 Q50 -2 100 5 L100 14 L0 14Z" fill="var(--black)"/>
      <path d="M0 8 Q50 0 100 7 L100 14 L0 14Z" fill="var(--red)"/>
    </svg>
  </article>
  <p class="caption card-caption">Business Card Front</p>

  <article class="item card-back">
    <div class="mark">
      <div class="mark-square"></div>
      <div class="mark-name">TL Estates</div>
      <div class="tagline">SALES · RENTALS · VALUATIONS</div>
    </div>
  </article>
  <p class="caption card-back-caption">Business Card Back</p>

  <article class="item letterhead letterhead-one">
    <div class="mark"><div class="mark-square"></div><div class="mark-name">TL Estates</div></div>
    <div class="contact">Suite # 17 Ashbury Business Centre<br>28 Calder Rd. Kingston 5<br>876-555-0142<br>dp@desmondparkes-example.com<br>www.desmondparkes-example.com</div>
    <div class="watermark"><div class="mark-square"></div><div class="mark-name">TL Estates</div></div>
    <svg class="wave" viewBox="0 0 100 20" preserveAspectRatio="none" height="24">
      <path d="M0 8 Q55 0 100 10 L100 20 L0 20Z" fill="var(--black)"/>
      <path d="M0 10 Q55 2 100 12 L100 20 L0 20Z" fill="var(--red)"/>
      <path d="M0 15 Q55 8 100 16 L100 20 L0 20Z" fill="var(--red-dark)"/>
    </svg>
  </article>

  <article class="item letterhead letterhead-two">
    <div class="watermark"><div class="mark-square"></div><div class="mark-name">TL Estates</div></div>
    <svg class="wave" viewBox="0 0 100 20" preserveAspectRatio="none" height="24">
      <path d="M0 8 Q55 0 100 10 L100 20 L0 20Z" fill="var(--black)"/>
      <path d="M0 10 Q55 2 100 12 L100 20 L0 20Z" fill="var(--red)"/>
      <path d="M0 15 Q55 8 100 16 L100 20 L0 20Z" fill="var(--red-dark)"/>
    </svg>
  </article>

  <article class="item envelope envelope-one">
    <div class="mark"><div class="mark-square"></div><div class="mark-name">TL Estates</div></div>
    <div class="watermark"><div class="mark-square"></div><div class="mark-name">TL Estates</div></div>
    <svg class="wave" viewBox="0 0 100 20" preserveAspectRatio="none" height="16">
      <path d="M0 9 Q50 0 100 8 L100 20 L0 20Z" fill="var(--black)"/>
      <path d="M0 11 Q50 2 100 10 L100 20 L0 20Z" fill="var(--red)"/>
    </svg>
  </article>

  <article class="item envelope envelope-two">
    <div class="mark"><div class="mark-square"></div><div class="mark-name">TL Estates</div></div>
    <div class="watermark"><div class="mark-square"></div><div class="mark-name">TL Estates</div></div>
    <svg class="wave" viewBox="0 0 100 20" preserveAspectRatio="none" height="16">
      <path d="M0 9 Q50 0 100 8 L100 20 L0 20Z" fill="var(--black)"/>
      <path d="M0 11 Q50 2 100 10 L100 20 L0 20Z" fill="var(--red)"/>
    </svg>
  </article>

  <article class="item envelope-back envelope-back-flap">
    <svg class="flap" viewBox="0 0 100 40" preserveAspectRatio="none" height="44">
      <path d="M0 0 L100 0 L100 8 Q50 48 0 8Z" fill="var(--black)"/>
      <path d="M0 6 Q50 42 100 6 L100 9 Q50 46 0 9Z" fill="var(--red)"/>
    </svg>
    <div class="mark"><div class="mark-square"></div><div class="mark-name">TL Estates</div></div>
    <svg class="wave" viewBox="0 0 100 20" preserveAspectRatio="none" height="28">
      <path d="M0 4 Q50 -4 100 4 L100 20 L0 20Z" fill="var(--red-dark)"/>
      <path d="M0 7 Q50 0 100 7 L100 20 L0 20Z" fill="var(--red)"/>
    </svg>
  </article>

  <article class="item envelope-back envelope-back-plain">
    <svg class="flap" viewBox="0 0 100 40" preserveAspectRatio="none" height="96">
      <path d="M0 0 L50 20 L100 0" fill="none" stroke="#d2d2d2" stroke-width=".5"/>
      <path d="M0 40 L42 16 M100 40 L58 16" fill="none" stroke="#dcdcdc" stroke-width=".4"/>
    </svg>
  </article>

</main>
</body>
</html>
```